Spark of Meadow Paddocks Business Cards with logo

Need a creative business card that pops. Colorful but professional. The attached logo should be included. We are a national horse racing partnership so we are in the equine business. Nothing cartoonlike or whimsical.

Target Market(s)

professionals - 40+

Contact Information for Business Card

Dana Whitlow
Director of Operations
27 Pinecrest Lane
Brookfield, KY 40599

Phone (555) 274-6183

FX: (555) 619-3047

email: dana@smpaddocks.example
smpaddocks.example

Requirements
Must have
• All information above should be on the business card including the website address. Professional yet creative
Nice to have
• an attention grabbing design. not boring. exciting.
Should not have
• cartoon like - whimsical.

```html
<!DOCTYPE html>
<html lang="en">
<head>
<meta charset="utf-8">
<title>Spark of Meadow Paddocks – Business Cards</title>
<link href="https://fonts.googleapis.com/css2?family=Fira+Sans:wght@400;600&display=swap" rel="stylesheet">
<style>
  :root {
    --navy: #2c3587;
    --navy-deep: #262f78;
    --gold: #c9a227;
    --paper: #ffffff;
    --backdrop: #e4e4e4;
  }
  * { box-sizing: border-box; margin: 0; padding: 0; }
  html, body {
    width: 1200px;
    height: 960px;
    overflow: hidden;
    background: var(--backdrop);
    font-family: "Fira Sans", sans-serif;
  }
  .canvas {
    position: relative;
    width: 1200px;
    height: 960px;
  }
  .card {
    position: absolute;
    left: 250px;
    width: 700px;
    height: 400px;
    box-shadow: 0 6px 18px rgba(0,0,0,0.12);
    overflow: hidden;
  }
  .card-front { top: 50px; background: var(--paper); }
  .card-back {
    top: 510px;
    background: radial-gradient(circle at 45% 20%, #3b46a3 0%, var(--navy) 45%, var(--navy-deep) 100%);
  }

  /* brand mark */
  .brand {
    position: absolute;
    display: flex;
    align-items: center;
    justify-content: center;
    border-radius: 50%;
    text-align: center;
    font-weight: 600;
    letter-spacing: 0.12em;
    text-transform: uppercase;
    line-height: 1.35;
  }
  .card-front .brand {
    left: 70px; top: 60px;
    width: 190px; height: 190px;
    border: 2px solid var(--gold);
    color: var(--navy);
    font-size: 17px;
  }
  .card-back .brand {
    left: 245px; top: 90px;
    width: 210px; height: 210px;
    border: 2px solid var(--gold);
    color: #ffffff;
    font-size: 18px;
  }

  .divider {
    position: absolute;
    left: 300px;
    top: 70px;
    width: 2px;
    height: 200px;
    background: var(--navy);
  }
  .divider::before {
    content: "";
    position: absolute;
    left: 0; top: 0;
    width: 2px; height: 24px;
    background: var(--gold);
  }

  .contact {
    position: absolute;
    left: 330px;
    top: 72px;
    color: var(--navy);
  }
  .contact-name {
    font-size: 28px;
    font-weight: 600;
    color: var(--gold);
    line-height: 1.1;
  }
  .contact-title {
    font-size: 17px;
    margin-bottom: 14px;
  }
  .contact-lines {
    list-style: none;
    font-size: 17px;
    line-height: 1.45;
  }

  .stripe-band {
    position: absolute;
    left: 0; bottom: 0;
    width: 100%;
    height: 30px;
    background: linear-gradient(90deg, var(--gold) 0%, var(--navy) 50%, var(--gold) 100%);
  }
</style>
</head>
<body>
<main class="canvas">
  <section class="card card-front" aria-label="Business card front">
    <div class="brand">Spark of<br>Meadow<br>Paddocks</div>
    <div class="divider"></div>
    <div class="contact">
      <p class="contact-name">Dana Whitlow</p>
      <p class="contact-title">Director of Operations</p>
      <ul class="contact-lines">
        <li>P (555) 274-6183</li>
        <li>F (555) 619-3047</li>
        <li>dana@smpaddocks.example</li>
        <li>smpaddocks.example</li>
        <li>27 Pinecrest Lane</li>
        <li>Brookfield, KY 40599</li>
      </ul>
    </div>
    <div class="stripe-band" role="img" aria-label="Gold and navy chevron stripe band"></div>
  </section>

  <section class="card card-back" aria-label="Business card back">
    <div class="brand">Spark of<br>Meadow<br>Paddocks</div>
  </section>
</main>
</body>
</html>
```